First of a series of workplace posters- our values statement

To produce a high quality poster of our values, we would like one in a3 and one in a4 both full colour
By utilising the supplied text , the intent is to produce a really striking poster for all our work places, which set out our company values. we are looking for really strong graphical elements which support the message visually . This will be the first of a series of posters, so we are looking to establish at stylistic theme for all with this one. for more on our business,

Target Market(s)

Internal and external audiences, our clients are all tier one companies

Requirements
Must have
• contemporary design rather than conservative, visually striking
• Must be clearly readable from a reasonable distance
Nice to have
• would be nice to tie in to the blue and greens of our logo in similar fashion to our website. www.kbtgreenworks.com
Should not have
• Difficult to read fonts,

```html
<!DOCTYPE html>
<html lang="en">
<head>
<meta charset="utf-8">
<title>KBT Greenworks – Our Values</title>
<link href="https://fonts.googleapis.com/css2?family=Rubik:wght@400;500&family=Rajdhani:wght@500&display=swap" rel="stylesheet">
<style>
  :root {
    --navy: #0b2f6b;
    --green: #62ad14;
    --pale: #eef6e2;
    --stage: #a7a9ac;
    --text: #e8eef8;
  }
  html, body {
    margin: 0;
    width: 933px;
    height: 1200px;
    overflow: hidden;
    background: var(--stage);
  }
  .poster {
    position: absolute;
    left: 75px;
    top: 40px;
    width: 760px;
    height: 1073px;
    background: var(--pale);
    overflow: hidden;
    box-shadow: 0 2px 8px rgba(0,0,0,0.25);
  }
  .poster-shapes {
    position: absolute;
    inset: 0;
  }
  .brand {
    position: absolute;
    left: 420px;
    top: 92px;
    display: flex;
    align-items: center;
    gap: 12px;
    font-family: "Rubik", sans-serif;
    font-weight: 500;
    font-size: 33px;
    color: var(--navy);
    white-space: nowrap;
  }
  .brand-dot {
    width: 30px;
    height: 30px;
    border-radius: 50%;
    background: var(--green);
  }
  .values-title {
    position: absolute;
    left: 44px;
    top: 304px;
    margin: 0;
    font-family: "Rubik", sans-serif;
    font-weight: 500;
    font-size: 28px;
    color: #fff;
  }
  .block {
    position: absolute;
    font-family: "Rajdhani", sans-serif;
    font-weight: 500;
    font-size: 11.4px;
    line-height: 15.2px;
    color: var(--text);
  }
  .block p { margin: 0; }
  .block .gap { margin-top: 15.2px; }
  .block h2 {
    margin: 0 0 14px;
    font-family: "Rubik", sans-serif;
    font-weight: 500;
    font-size: 14px;
    line-height: 18px;
    color: #fff;
  }
  .col-left { left: 44px; width: 345px; }
  .col-right { left: 405px; width: 305px; }
</style>
</head>
<body>
<main class="poster">
  <svg class="poster-shapes" viewBox="0 0 760 1073" width="760" height="1073" aria-hidden="true">
    <polygon fill="var(--navy)" points="0,125 676,468 700,382 760,372 760,1073 0,1073"/>
    <polygon fill="var(--green)" points="0,0 115,0 678,468 0,82"/>
    <polygon fill="var(--navy)" points="115,0 190,0 680,468"/>
    <polygon fill="var(--green)" points="645,338 760,250 760,305"/>
    <polygon fill="var(--green)" points="655,370 760,320 760,585 695,380"/>
    <polygon fill="var(--green)" points="148,1073 760,918 760,960 262,1073"/>
    <polygon fill="var(--pale)" points="330,1073 760,1016 760,1073"/>
  </svg>

  <div class="brand"><span class="brand-dot"></span>KBT Greenworks</div>

  <h1 class="values-title">Our Values</h1>
  <div class="block col-left" style="top:352px">
    <p>These are the key things we value, we measure all our daily activi-<br>ties against these. They define the way we do business.</p>
  </div>

  <section class="block col-left" style="top:404px">
    <h2>We value our people above everything else</h2>
    <p>We demonstrate this by:</p>
    <p class="gap">§ Providing safe, positive, enjoyable workplaces where everyone<br>feels valued and respected.</p>
    <p>§ Providing careers, not jobs, we grow together.</p>
    <p>§ Encouraging inclusion, participation and collaboration.</p>
    <p>§ Recognising and rewarding contribution and excellence.</p>
    <p>§ Supporting our people through tough times.</p>
    <p>§ Fostering healthy work life balance.</p>
  </section>

  <section class="block col-left" style="top:590px">
    <h2>All our workplaces are safe work places</h2>
    <p>There is nothing more important to us than our team members<br>going home healthy and safe every day, we won't accept anything<br>less. We believe workplace<br>safety is a management choice, by providing safe work systems<br>and education we achieve our daily goal of Zero Harm.<br>We:</p>
    <p class="gap">§ Take the time to make our work areas safe, whatever it takes.</p>
    <p>§ Don't accept shortcuts.</p>
    <p>§ Look out for each other.</p>
    <p>§ Investigate our incidents and learn from them, no repeats.</p>
    <p>§ Are constantly looking for ways to improve the safety of our<br>workplaces and the health of our team members.</p>
    <p>§ Think safe, work safe, go home safe!</p>
  </section>

  <section class="block col-left" style="top:857px">
    <h2>The planet benefits from our existence</h2>
    <p>We are relentlessly pursuing our objective of providing our clients<br>with pathways to sustainable development. To achieve our vision<br>we</p>
    <p>§ Minimise our environmental impact in everything we do.</p>
    <p>§ Actively develop and promote world's best practices in<br>rehabilitation of disturbed land.</p>
  </section>

  <section class="block col-right" style="top:471px">
    <h2>We are proud of who we are</h2>
    <p>Our reputation means the world to us. We:</p>
    <p>§ Treat everyone with respect, and we expect it in return.</p>
    <p>§ Follow the rules</p>
    <p>§ Do what we say we will do.</p>
    <p>§ Own our mistakes and we fix them.</p>
    <p>§ Are trustworthy and transparent.</p>
  </section>

  <section class="block col-right" style="top:616px">
    <h2>We set the standard</h2>
    <p>We are uncompromising on quality.<br>We are the best at what we do, and we do what we are<br>best at.<br>We are always improving.</p>
  </section>

  <section class="block col-right" style="top:731px">
    <h2>We succeed together</h2>
    <p>We believe in win-win relationships. When our Business is<br>profitable everyone benefits, our shareholders, employees,<br>clients, suppliers and the community.<br>AT KBT We:</p>
    <p>§ work as a team, we get it done together</p>
    <p>§ are building on our success and growing together</p>
    <p>§ choose to work with employees, customers, and suppliers<br>who fit our values.</p>
  </section>
</main>
</body>
</html>
```